4"x6" Postcards Grand opening promotion for Med Spa

Put our logo on the forehead of mask. Not all photos of mask needed. Just what you think is necessary. Some ideas of what to write is below

🌟 GRAND OPENING SPECIAL 🌟
Celebrate with Lumora Medical Aesthetics!

We’re officially open in Maple Terrace, and to celebrate, we’re giving new clients a FREE Red-Light Therapy Mask β€” a $247 value!

✨ NEW CLIENT EXCLUSIVE
Get your skin glowing with this luxurious Red-Light Therapy Mask, yours FREE with select purchases or membership sign-ups β€”
a $247 gift, absolutely on us!

βœ” Boosts collagen production
βœ” Reduces redness & inflammation
βœ” Enhances skin tone and texture
βœ” Non-invasive, relaxing & easy to use

πŸ“ Visit us at:
Studio Vantra – Rooms 21 & 22
4817 Cedar Vale Rd #340, Irving, TX 75038

πŸ•’ Hours:
Thursday & Friday: 10 AM – 5 PM
Saturday: 10:30 AM – 2 PM

πŸ“ž Spots are limited – don’t miss out on your $247 gift!
Call 469-318-4096 to schedule your appointment.

🌐 https://lumoramedicalaesthetics.example | @lumoramedicalaesthetics

Limited-time offer. While supplies last. Free mask available with specific purchases or membership sign-ups only.

```html
<!DOCTYPE html>
<html lang="en">
<head>
<meta charset="UTF-8">
<title>Lumora Medical Aesthetics – Grand Opening Postcard</title>
<link href="https://fonts.googleapis.com/css2?family=Cinzel:wght@700&family=Poppins:wght@400;500;700&display=swap" rel="stylesheet">
<style>
  :root {
    --backdrop: #3b3a36;
    --charcoal: #2a2627;
    --charcoal-light: #4a4546;
    --ink: #2b2b2b;
    --white: #ffffff;
    --red: #e0505a;
    --gold: #bfa35f;
    --gold-text: #8a7348;
  }
  * { margin: 0; padding: 0; box-sizing: border-box; }
  html, body { width: 896px; height: 1200px; overflow: hidden; }
  body {
    background: var(--backdrop);
    font-family: "Poppins", sans-serif;
    position: relative;
  }
  .card {
    position: absolute;
    left: 60px;
    width: 780px;
    height: 521px;
    background: var(--white);
    overflow: hidden;
  }
  .card--front { top: 56px; }
  .card--back { top: 624px; }

  .band {
    position: absolute;
    left: 0;
    width: 100%;
    background: radial-gradient(ellipse at 40% 50%, var(--charcoal-light) 0%, var(--charcoal) 70%);
  }
  .abs { position: absolute; line-height: 1; white-space: nowrap; }

  /* Front */
  .front-header { top: 0; height: 151px; }
  .headline {
    font-family: "Cinzel", serif;
    font-weight: 700;
    color: var(--white);
    font-size: 42px;
    left: 28px;
    letter-spacing: 0.5px;
  }
  .celebrate { left: 28px; top: 113px; font-size: 18px; font-weight: 500; color: var(--white); }
  .brand-name {
    font-family: "Poppins", sans-serif;
    font-weight: 500;
    text-transform: uppercase;
    display: flex;
    align-items: center;
    gap: 10px;
  }
  .brand-name .dot { width: 12px; height: 12px; border-radius: 50%; flex: none; }
  .brand-name--light { color: var(--white); font-size: 13px; letter-spacing: 3px; right: 20px; top: 60px; }
  .brand-name--light .dot { background: var(--white); }
  .brand-name--dark { color: var(--ink); font-size: 13px; letter-spacing: 4px; left: 34px; top: 60px; }
  .brand-name--dark .dot { background: var(--gold-text); }

  .photo-front {
    left: 420px; top: 151px; width: 360px; height: 308px;
    background: linear-gradient(100deg, #ffffff 0%, #f6c9c6 30%, #ef9a9a 55%, #f3d6cf 80%, #f7e6e0 100%);
  }
  .offer-line { left: 27px; font-size: 37px; font-weight: 500; color: var(--ink); letter-spacing: 0.5px; }
  .offer-line--red { color: var(--red); }
  .body-copy { left: 24px; font-size: 18px; color: var(--ink); }
  .body-note { left: 24px; font-size: 15px; color: var(--gold-text); }
  .schedule { left: 28px; top: 424px; font-size: 18px; color: var(--ink); }

  .front-footer { top: 459px; height: 62px; }
  .phone-icon { position: absolute; }
  .front-phone { left: 60px; top: 15px; font-size: 30px; font-weight: 700; color: var(--white); }
  .front-web { left: 284px; top: 23px; font-size: 14px; color: var(--white); }
  .social { left: 590px; font-size: 11px; color: var(--white); display: flex; align-items: center; gap: 8px; }
  .social .dot { width: 8px; height: 8px; border-radius: 50%; background: var(--white); flex: none; }

  /* Back */
  .stamp-box { left: 694px; top: 33px; width: 58px; height: 58px; border: 2px solid var(--gold); }
  .address-line { position: absolute; left: 416px; width: 336px; height: 2px; background: var(--gold); }
  .value { left: 34px; top: 121px; font-size: 50px; font-weight: 500; color: var(--red); }
  .product { left: 34px; top: 176px; font-size: 21px; font-weight: 500; color: var(--gold); }
  .benefits { position: absolute; left: 34px; top: 208px; list-style: none; }
  .benefits li { display: flex; align-items: center; gap: 8px; font-size: 18px; color: var(--ink); height: 21.6px; }
  .red-disc {
    position: absolute; left: 458px; top: 221px; width: 292px; height: 292px;
    border-radius: 50%; background: var(--red);
  }
  .back-footer { top: 316px; height: 205px; }
  .photo-back {
    left: 483px; top: 225px; width: 236px; height: 176px; border-radius: 30px 30px 60px 60px;
    background: linear-gradient(180deg, #3a3839 0%, #252324 100%);
  }
  .label { left: 34px; font-size: 17px; font-weight: 700; color: var(--gold); }
  .info { left: 34px; font-size: 17.5px; color: var(--white); }
  .phone-box {
    position: absolute; left: 471px; top: 419px; width: 252px; height: 42px;
    background: var(--gold); display: flex; align-items: center; justify-content: center; gap: 10px;
    font-size: 27px; font-weight: 700; color: var(--white);
  }
  .back-web { left: 436px; width: 322px; text-align: center; top: 476px; font-size: 15px; color: var(--white); }
</style>
</head>
<body>

<section class="card card--front">
  <div class="band front-header">
    <div class="abs headline" style="top:24px;">GRAND OPENING</div>
    <div class="abs headline" style="top:70px;">SPECIAL</div>
    <div class="abs celebrate">Celebrate with Lumora Medical Aesthetics!</div>
    <div class="abs brand-name brand-name--light"><span class="dot"></span>Lumora Medical Aesthetics</div>
  </div>

  <div class="abs photo-front" role="img" aria-label="Red-light therapy mask with the Lumora name on its forehead, beside a woman bathed in red light"></div>

  <div class="abs offer-line" style="top:186px;">A FREE RED-LIGHT</div>
  <div class="abs offer-line" style="top:231px;">THERAPY MASK</div>
  <div class="abs offer-line offer-line--red" style="top:276px;">– A $247 VALUE!</div>

  <div class="abs body-copy" style="top:344px;">We’re officially open in Maple Terrace, and</div>
  <div class="abs body-copy" style="top:366px;">to celebrate, we’re giving new clients</div>
  <div class="abs body-note" style="top:389px;">(with select purchases or membership sign-ups)</div>
  <div class="abs schedule">Schedule your appointment</div>

  <div class="band front-footer">
    <svg class="phone-icon" style="left:27px;top:16px;" width="22" height="22" viewBox="0 0 24 24" aria-hidden="true">
      <path fill="#e0505a" d="M6.6 10.8c1.4 2.8 3.8 5.1 6.6 6.6l2.2-2.2c.3-.3.7-.4 1-.2 1.1.4 2.3.6 3.6.6.6 0 1 .4 1 1V20c0 .6-.4 1-1 1C10.6 21 3 13.4 3 4c0-.6.4-1 1-1h3.5c.6 0 1 .4 1 1 0 1.3.2 2.5.6 3.6.1.3 0 .7-.2 1L6.6 10.8z"/>
    </svg>
    <div class="abs front-phone">469-318-4096</div>
    <div class="abs front-web">www.lumoramedicalaesthetics.example</div>
    <div class="abs social" style="top:15px;"><span class="dot"></span>Lumora Medical Aesthetics</div>
    <div class="abs social" style="top:33px;"><span class="dot"></span>@lumoramedicalaesthetics</div>
  </div>
</section>

<section class="card card--back">
  <div class="abs brand-name brand-name--dark"><span class="dot"></span>Lumora Medical Aesthetics</div>
  <div class="abs stamp-box"></div>
  <div class="address-line" style="top:132px;"></div>
  <div class="address-line" style="top:188px;"></div>

  <div class="abs value">$247 VALUE!</div>
  <div class="abs product">RED-LIGHT THERAPY MASK</div>
  <ul class="benefits">
    <li><svg width="14" height="14" viewBox="0 0 16 16" aria-hidden="true"><circle cx="8" cy="8" r="6.5" fill="none" stroke="#bfa35f" stroke-width="1.5"/><path d="M4.8 8.2l2.2 2.2 4.4-4.6" fill="none" stroke="#bfa35f" stroke-width="1.6"/></svg>Boosts collagen production</li>
    <li><svg width="14" height="14" viewBox="0 0 16 16" aria-hidden="true"><circle cx="8" cy="8" r="6.5" fill="none" stroke="#bfa35f" stroke-width="1.5"/><path d="M4.8 8.2l2.2 2.2 4.4-4.6" fill="none" stroke="#bfa35f" stroke-width="1.6"/></svg>Reduces redness &amp; inflammation</li>
    <li><svg width="14" height="14" viewBox="0 0 16 16" aria-hidden="true"><circle cx="8" cy="8" r="6.5" fill="none" stroke="#bfa35f" stroke-width="1.5"/><path d="M4.8 8.2l2.2 2.2 4.4-4.6" fill="none" stroke="#bfa35f" stroke-width="1.6"/></svg>Enhances skin tone and texture</li>
    <li><svg width="14" height="14" viewBox="0 0 16 16" aria-hidden="true"><circle cx="8" cy="8" r="6.5" fill="none" stroke="#bfa35f" stroke-width="1.5"/><path d="M4.8 8.2l2.2 2.2 4.4-4.6" fill="none" stroke="#bfa35f" stroke-width="1.6"/></svg>Non-invasive, relaxing &amp; easy to use</li>
  </ul>

  <div class="red-disc"></div>

  <div class="band back-footer">
    <div class="abs label" style="top:24px;">VISIT US AT:</div>
    <div class="abs info" style="top:45px;">Studio Vantra – Rooms 21 &amp; 22</div>
    <div class="abs info" style="top:67px;">4817 Cedar Vale Rd #340, Irving, TX 75038</div>
    <div class="abs label" style="top:117px;">HOURS:</div>
    <div class="abs info" style="top:138px;">Thursday &amp; Friday: 10 AM – 5 PM</div>
    <div class="abs info" style="top:159px;">Saturday: 10:30 AM – 2 PM</div>
  </div>

  <div class="abs photo-back" role="img" aria-label="Front view of the black red-light therapy mask with the Lumora name on its forehead"></div>

  <div class="phone-box">
    <svg width="22" height="22" viewBox="0 0 24 24" aria-hidden="true">
      <path fill="#ffffff" d="M6.6 10.8c1.4 2.8 3.8 5.1 6.6 6.6l2.2-2.2c.3-.3.7-.4 1-.2 1.1.4 2.3.6 3.6.6.6 0 1 .4 1 1V20c0 .6-.4 1-1 1C10.6 21 3 13.4 3 4c0-.6.4-1 1-1h3.5c.6 0 1 .4 1 1 0 1.3.2 2.5.6 3.6.1.3 0 .7-.2 1L6.6 10.8z"/>
    </svg>
    469-318-4096
  </div>
  <div class="abs back-web">www.lumoramedicalaesthetics.example</div>
</section>

</body>
</html>
```